Need a business card design for a new business

The business is going to be called "The Maple Lectern" - it is an online training company that provides Instructor Lead training to students at any destination in the world
The reference to cloud is the internet and classroom reference will be a computer at the students and instructors end

We will need a Web site and stationary and advertising material developed over time but for now require the business cards only

So if we are happy with the business card then we will use the same designers for the other requirments of the business as it evolves

Industry/Entity Type

Advertising

```html
<!DOCTYPE html>
<html lang="en">
<head>
<meta charset="utf-8">
<title>The Maple Lectern – Business Card</title>
<link rel="stylesheet" href="https://fonts.googleapis.com/css2?family=Pinyon+Script&family=Tinos&display=swap">
<style>
  :root {
    --card-white: #ffffff;
    --frame: #3a3a3a;
    --ink: #2e2e2e;
    --sky-top: #6e9fcc;
    --sky-mid: #b9cbdc;
    --sky-low: #d9e0e8;
    --arrow-blue: #2f64a0;
    --arrow-edge: #1d2e45;
    --globe-light: #7cc4ee;
    --globe-deep: #3f74c2;
    --globe-land: #37a24f;
    --figure-grey: #4a4a4a;
    --figure-bg: #eeeeee;
  }
  html, body {
    margin: 0;
    padding: 0;
    width: 1200px;
    height: 684px;
    overflow: hidden;
    background: var(--card-white);
  }
  .business-card {
    display: block;
    width: 1200px;
    height: 684px;
  }
  .brand-name {
    font-family: "Pinyon Script", cursive;
    font-size: 124px;
    fill: var(--ink);
  }
  .tagline {
    font-family: "Tinos", serif;
    font-size: 98px;
    fill: var(--ink);
  }
  .arrow {
    fill: var(--arrow-blue);
    stroke: var(--arrow-edge);
    stroke-width: 1.5;
  }
  .card-frame {
    fill: none;
    stroke: var(--frame);
    stroke-width: 3;
  }
  .cloud-divide {
    fill: none;
    stroke: var(--frame);
    stroke-width: 1.5;
  }
</style>
</head>
<body>
<svg class="business-card" viewBox="0 0 1200 684" xmlns="http://www.w3.org/2000/svg" aria-labelledby="card-title">
  <title id="card-title">The Maple Lectern – World wide e-learning</title>
  <defs>
    <linearGradient id="sky-fill" x1="0" y1="0" x2="0" y2="1">
      <stop offset="0" stop-color="var(--sky-top)"/>
      <stop offset="0.35" stop-color="var(--sky-mid)"/>
      <stop offset="1" stop-color="var(--sky-low)"/>
    </linearGradient>
    <radialGradient id="globe-fill" cx="0.6" cy="0.35" r="0.75">
      <stop offset="0" stop-color="var(--globe-light)"/>
      <stop offset="0.45" stop-color="var(--globe-land)"/>
      <stop offset="1" stop-color="var(--globe-deep)"/>
    </radialGradient>
  </defs>

  <rect class="card-background" x="0" y="0" width="1200" height="684" fill="var(--card-white)"/>

  <path class="sky-area" role="img" aria-label="Photograph of a blue sky with white clouds"
        d="M0 0 H684 C600 120 540 300 590 470 C630 580 730 650 838 684 H0 Z"
        fill="url(#sky-fill)"/>
  <path class="cloud-divide" d="M684 0 C600 120 540 300 590 470 C630 580 730 650 838 684"/>

  <text class="brand-name" x="604" y="180" text-anchor="middle" textLength="960" lengthAdjust="spacingAndGlyphs">The Maple Lectern</text>

  <g class="connection-arrows">
    <path class="arrow arrow-left" d="M243 334 L410 256 L410 299 L520 299 L520 370 L410 370 L410 408 Z"/>
    <path class="arrow arrow-right" d="M906 334 L741 256 L741 299 L620 299 L620 370 L741 370 L741 408 Z"/>
  </g>

  <circle class="globe" role="img" aria-label="Illustrated globe showing the Americas"
          cx="566" cy="334" r="105" fill="url(#globe-fill)"/>

  <rect class="student-at-computer" role="img" aria-label="Silhouette of a student working at a desktop computer"
        x="875" y="251" width="307" height="216" fill="var(--figure-bg)"/>

  <text class="tagline" x="595" y="587" text-anchor="middle" textLength="1010" lengthAdjust="spacingAndGlyphs">World wide e-learning</text>

  <rect class="card-frame" x="1.5" y="1.5" width="1197" height="681"/>
</svg>
</body>
</html>
```